Engineering Consultant Business Card

I'm starting a new business as a high-end engineering consultant in a niche field. I've attached the jpg for my logo plus the branding guideline document that I've been following. You can see my business website here: www.tarvikworks.com
I'd like a business card that has the logo on one side, then the other side has (in any order): Tarvik Works, Inc.
Dana Whitlock
President and Chief EMC Engineer
www.tarvikworks.com
dana@tarvikworks.com
Optional: motto "We will solve your EMC problems as early as possible—ideally before they even start."
I'm not planning on including a phone number
Target Market(s)
Businesses, especially makers of electronics hardware
Industry/Entity Type
Electrical engineering
Contact Information for Business Card
Company name, my name, website, email

```html
<!DOCTYPE html>
<html lang="en">
<head>
<meta charset="utf-8">
<title>Tarvik Works, Inc. – Business Card</title>
<link href="https://fonts.googleapis.com/css2?family=Poppins:wght@400;600&display=swap" rel="stylesheet">
<style>
  :root {
    --backdrop: #3b3b3b;
    --card-blue: #30479a;
    --ink-white: #ffffff;
    --card-shadow: rgba(0, 0, 0, 0.45);
  }
  * { box-sizing: border-box; margin: 0; padding: 0; }
  html, body {
    width: 1200px;
    height: 689px;
    overflow: hidden;
    background: var(--backdrop);
    font-family: "Poppins", sans-serif;
    color: var(--ink-white);
  }
  .card-set {
    width: 1200px;
    height: 689px;
    display: flex;
    align-items: center;
    justify-content: center;
    gap: 50px;
  }
  .card {
    width: 525px;
    height: 300px;
    background: var(--card-blue);
    border-radius: 22px;
    box-shadow: 0 18px 40px var(--card-shadow);
    display: flex;
    flex-direction: column;
    align-items: center;
    justify-content: center;
    text-align: center;
  }
  .brand-mark {
    display: flex;
    align-items: center;
    gap: 12px;
    font-weight: 600;
    color: var(--ink-white);
  }
  .brand-mark__dot {
    border-radius: 50%;
    border: 5px solid var(--ink-white);
  }
  .card--front .brand-mark { font-size: 34px; margin-bottom: 34px; }
  .card--front .brand-mark__dot { width: 46px; height: 46px; }
  .motto {
    font-size: 15px;
    line-height: 1.5;
    font-weight: 400;
    max-width: 400px;
  }
  .card--back .brand-mark { font-size: 26px; margin-bottom: 26px; }
  .card--back .brand-mark__dot { width: 36px; height: 36px; border-width: 4px; }
  .person-name {
    font-size: 26px;
    font-weight: 600;
    line-height: 1.2;
  }
  .person-title {
    font-size: 14px;
    font-weight: 400;
    margin-top: 4px;
    margin-bottom: 18px;
  }
  .contact-list { list-style: none; font-size: 14px; line-height: 1.7; }
  .contact-list li { display: flex; align-items: center; gap: 8px; }
  .contact-icon { width: 16px; height: 16px; flex: none; }
</style>
</head>
<body>
  <main class="card-set">
    <section class="card card--front" aria-label="Card front">
      <div class="brand-mark">
        <span class="brand-mark__dot" aria-hidden="true"></span>
        <span class="brand-mark__name">Tarvik Works</span>
      </div>
      <p class="motto">We will solve your EMC problems as early as possible—ideally before they even start.”</p>
    </section>

    <section class="card card--back" aria-label="Card back">
      <div class="brand-mark">
        <span class="brand-mark__dot" aria-hidden="true"></span>
        <span class="brand-mark__name">Tarvik Works</span>
      </div>
      <h1 class="person-name">Dana Whitlock</h1>
      <p class="person-title">President and Chief EMC Engineer</p>
      <ul class="contact-list">
        <li>
          <svg class="contact-icon" viewBox="0 0 16 16" aria-hidden="true">
            <rect x="1" y="3" width="14" height="10" fill="var(--ink-white)"/>
            <path d="M1 3 L8 9 L15 3" fill="none" stroke="var(--card-blue)" stroke-width="1.4"/>
          </svg>
          <span>dana@tarvikworks.com</span>
        </li>
        <li>
          <svg class="contact-icon" viewBox="0 0 16 16" aria-hidden="true" fill="none" stroke="var(--ink-white)" stroke-width="1.4">
            <circle cx="8" cy="8" r="6.5"/>
            <ellipse cx="8" cy="8" rx="3" ry="6.5"/>
            <line x1="1.5" y1="8" x2="14.5" y2="8"/>
          </svg>
          <span>www.tarvikworks.com</span>
        </li>
      </ul>
    </section>
  </main>
</body>
</html>
```